Newsletter Design Project

I need a new design for a monthly newsletter that I do for Marbury Lane Open College Ipswich. I have been doing the same thing since 2009. We are based in Brisbane and we run classes for semi retired and retired people. I write about social activities, class activities, vacancies etc. I take photos and include them we hhave a logo that I always use. and would just like the newsletter to look different and fresh. The logo is Blue

```html
<!DOCTYPE html>
<html lang="en">
<head>
<meta charset="utf-8">
<title>E Newsletter – May 2013</title>
<link href="https://fonts.googleapis.com/css2?family=Tinos:ital,wght@0,400;0,700;1,400&display=swap" rel="stylesheet">
<style>
  :root {
    --navy: #0b1466;
    --navy-deep: #070d4a;
    --band: #5f7fe0;
    --band-soft: #a9b9f2;
    --lavender: #c9d0f2;
    --paper: #ffffff;
    --ink: #10174f;
    --title: #1c2a7a;
    --label: #3a63c9;
    --panel: #d5d8ee;
    --panel-edge: #c0c5e4;
    --label-strip: #eef0fb;
  }
  * { box-sizing: border-box; margin: 0; padding: 0; }
  html, body { width: 848px; height: 1200px; overflow: hidden; background: var(--paper); }
  body { font-family: "Tinos", "Times New Roman", serif; color: var(--ink); }

  .newsletter {
    position: relative;
    width: 848px; height: 1200px;
    overflow: hidden;
    background: radial-gradient(ellipse 70% 55% at 50% 42%, #ffffff 0%, #f3f5fd 45%, var(--lavender) 100%);
  }
  .backdrop { position: absolute; inset: 0; width: 848px; height: 1200px; }

  .brand {
    position: absolute; left: 596px; top: 26px; width: 214px; height: 88px;
    background: var(--paper);
    display: flex; align-items: center; gap: 10px; padding: 0 12px;
  }
  .brand-mark { width: 16px; height: 16px; background: var(--navy); flex: none; }
  .brand-name { font-size: 17px; line-height: 1.15; font-weight: 700; color: var(--navy); }

  .masthead { position: absolute; left: 0; right: 0; top: 128px; text-align: center; color: var(--title); }
  .masthead-title { font-size: 64px; font-weight: 400; line-height: 1; letter-spacing: 0.5px; }
  .masthead-date { font-size: 40px; line-height: 1.1; margin-top: 2px; color: #3d4fb3; }
  .masthead-date .spark { font-size: 18px; vertical-align: middle; margin: 0 8px; }

  .section { position: absolute; left: 67px; right: 40px; }
  .section-heading {
    display: flex; align-items: center; gap: 12px;
    font-size: 29px; font-weight: 700; line-height: 1; color: var(--ink);
    margin-left: 10px;
  }
  .section-heading.small { font-size: 22px; }
  .bullet {
    width: 16px; height: 16px; background: var(--navy); flex: none;
    border: 2px solid var(--navy); position: relative;
  }
  .bullet::after {
    content: ""; position: absolute; inset: 3px; border: 1.5px solid #ffffff;
  }
  .section-body { font-size: 17.5px; line-height: 1.3; margin-top: 4px; }

  .term { top: 252px; }
  .president { top: 330px; }
  .bus { top: 512px; }
  .bus .section-body { margin-top: 10px; }
  .district { top: 640px; }

  .district-entry { position: absolute; left: 64px; width: 572px; }
  .district-label {
    background: linear-gradient(90deg, var(--label-strip), rgba(238,240,251,0.3));
    font-size: 18px; font-weight: 700; padding: 1px 10px; color: var(--ink);
  }
  .district-label .place { color: var(--label); }
  .district-text {
    background: var(--panel); border: 1px solid var(--panel-edge);
    font-size: 15.5px; line-height: 1.32; padding: 10px 12px;
  }
  .wynnum { top: 685px; }
  .wynnum .district-text { height: 162px; }
  .logan { top: 898px; }
  .logan .district-text { height: 164px; }

  .photo-frame {
    position: absolute; background: var(--navy-deep); padding: 7px;
    box-shadow: 0 0 0 1px var(--band-soft);
  }
  .photo-frame .photo { width: 100%; height: 100%; border: 2px solid #7d93e6; }
  .wynnum-photo { left: 673px; top: 681px; width: 134px; height: 148px; }
  .wynnum-photo .photo { background: linear-gradient(160deg, #b7b0a8 0%, #e3ddd6 45%, #8f6d5a 100%); }
  .logan-photo { left: 681px; top: 898px; width: 131px; height: 149px; }
  .logan-photo .photo { background: linear-gradient(170deg, #f2f0ee 0%, #c58f7a 45%, #7a4a39 100%); }
</style>
</head>
<body>
<main class="newsletter">
  <svg class="backdrop" viewBox="0 0 848 1200" aria-hidden="true">
    <polygon points="0,0 848,0 848,6 160,6 0,60" fill="var(--navy)"/>
    <polygon points="0,0 230,0 0,140" fill="var(--navy)"/>
    <polygon points="150,6 600,6 0,240 0,150" fill="var(--band-soft)" opacity="0.55"/>
    <polygon points="0,140 230,6 290,6 0,190" fill="var(--band)" opacity="0.7"/>
    <polygon points="0,60 0,1200 14,1200 14,60" fill="var(--band)" opacity="0.55"/>
    <polygon points="0,1120 250,1200 0,1200" fill="var(--navy)"/>
    <polygon points="0,1060 420,1200 250,1200 0,1120" fill="var(--band)" opacity="0.6"/>
    <polygon points="848,1100 848,1200 560,1200" fill="var(--band)" opacity="0.65"/>
    <polygon points="848,1150 848,1200 700,1200" fill="var(--navy)"/>
    <polygon points="834,0 848,0 848,1200 834,1200" fill="var(--band-soft)" opacity="0.5"/>
  </svg>

  <div class="brand">
    <span class="brand-mark"></span>
    <span class="brand-name">Marbury Lane Open College Ipswich</span>
  </div>

  <header class="masthead">
    <h1 class="masthead-title">E Newsletter</h1>
    <p class="masthead-date"><span class="spark">✦</span>May 2013<span class="spark">✦</span></p>
  </header>

  <section class="section term">
    <h2 class="section-heading"><span class="bullet"></span>Term 2:</h2>
    <p class="section-body">Did you realise that we are nearly half way through this term? 2013 seems to be racing</p>
  </section>

  <section class="section president">
    <h2 class="section-heading"><span class="bullet"></span>Message from the President:</h2>
    <p class="section-body">Graham says “I have access to a large group of book publishers—<br>
    Larkfield House, Brennan &amp; Sons, Riverbend Press, Thornbury Press and many more— who would like older<br>
    people to review their latest books. These include fiction, non fiction and poetry.”<br>
    If you would like to write a book review (and keep the new publications as your own) please<br>
    contact the President, Graham Whitby at gwhitby@oakmail.com.au</p>
  </section>

  <section class="section bus">
    <h2 class="section-heading small"><span class="bullet"></span>Bus Review from the Moreton Bay Transit Office. The link is as follows</h2>
    <p class="section-body">http//www.moretontransit.org.au/traffic-transport/public-transport/buses/bus-network-<br>review/index.htm<br>
    This will allow you to assess if you need to object to any of the changes.</p>
  </section>

  <section class="section district">
    <h2 class="section-heading"><span class="bullet"></span>District information:</h2>
  </section>

  <article class="district-entry wynnum">
    <h3 class="district-label"><span class="place">Wynnum:</span> from Marion Keller</h3>
    <p class="district-text">“Our Wynnum Calligraphy Group recently celebrated the 80th birthday of one of our long time members, Nola Baxter. We had a special morning tea after our Calligraphy class complete with birthday cake and a Birthday Tiara for Nola.”<br>Happy birthday Nola</p>
  </article>
  <div class="photo-frame wynnum-photo"><div class="photo" role="img" aria-label="Photo of a member wearing a birthday tiara beside her birthday cake"></div></div>

  <article class="district-entry logan">
    <h3 class="district-label"><span class="place">Logan:</span> from Helen Archer</h3>
    <p class="district-text">“Logan District students are sad that we will soon lose Rosalind Hale who has taught Spanish in her inimitable style to hundreds of students in the city and in Logan. Ros is moving to Victoria Point at the end of May and plans to teach Spanish for Redlands Open College. Our loss is their gain and we hope Ros will be very happy in her new home. Meanwhile students are hoping to find another Spanish tutor for Logan. Any offers?”</p>
  </article>
  <div class="photo-frame logan-photo"><div class="photo" role="img" aria-label="Portrait photo of the departing Spanish tutor"></div></div>
</main>
</body>
</html>
```